Pest Control Company needs business card!

Hi there, we need a business card designed for our new Pest Control Company. Ideally this card will be simple, yet feel elegant and high end. We want to use the colours Orange, Black and White. Please see our attached logo for the exact colours.

Business card details:

Phone - 0461 275 804
Name - Gavin Holloway
Email - Info@steadfastverminguard.com.au

We would also like to include the following list with dot points:

SERVICES / INSPECTIONS

Termites, Wood Borers, Ants, Cockroaches, Spiders, Fleas, Mice, Rats, Bed Bugs, & More!

```html
<!DOCTYPE html>
<html lang="en">
<head>
<meta charset="utf-8">
<title>Steadfast Vermin Guard – Business Card</title>
<link rel="stylesheet" href="https://fonts.googleapis.com/css2?family=Montserrat:wght@600;800&family=Roboto:wght@400;500&display=swap">
<style>
  :root {
    --orange: #f47b16;
    --orange-deep: #e26f10;
    --card-black: #1e1e20;
    --white: #ffffff;
    --red: #e4222a;
    --rule: #6a6a6c;
    --backdrop: #2b2b2d;
  }
  * { box-sizing: border-box; margin: 0; padding: 0; }
  html, body { width: 1200px; height: 1108px; overflow: hidden; background: var(--backdrop); }
  .canvas { position: relative; width: 1200px; height: 1108px; }

  .card {
    position: absolute; top: 209px; width: 420px; height: 690px;
    border-radius: 28px; overflow: hidden;
  }
  .card--front { left: 150px; background: var(--card-black); color: var(--white); text-align: center; }
  .card--back { left: 630px; background: var(--orange); }

  .brand {
    margin: 96px auto 0; display: flex; align-items: center; justify-content: center; gap: 14px;
  }
  .brand__name {
    font-family: "Montserrat", sans-serif; font-weight: 800; color: var(--white);
    font-size: 40px; line-height: 1.0; text-transform: uppercase; text-align: left; letter-spacing: -0.5px;
  }
  .brand__dot { width: 26px; height: 26px; border-radius: 50%; background: var(--white); flex: none; }

  .holder {
    margin-top: 74px; font-family: "Montserrat", sans-serif; font-weight: 600;
    color: var(--orange); font-size: 30px; text-transform: uppercase; letter-spacing: 0.5px;
  }

  .contact-rule { display: flex; align-items: center; justify-content: center; gap: 8px; margin-top: 28px; }
  .contact-rule__line { width: 80px; height: 1px; background: var(--rule); }
  .icon {
    width: 34px; height: 34px; border-radius: 6px; background: var(--orange);
    display: flex; align-items: center; justify-content: center;
  }
  .icon svg { width: 22px; height: 22px; }

  .contact { margin-top: 14px; font-family: "Roboto", sans-serif; font-size: 21px; line-height: 1.35; }

  .divider { width: 300px; height: 1px; background: var(--rule); margin: 14px auto 0; }

  .services__title {
    margin-top: 18px; font-family: "Roboto", sans-serif; font-weight: 500;
    color: var(--orange); font-size: 26px; text-transform: uppercase;
  }
  .services__list { margin-top: 8px; font-family: "Roboto", sans-serif; font-size: 23px; line-height: 1.4; }
  .bullet { display: inline-block; width: 13px; height: 13px; border-radius: 50%; background: var(--red); margin: 0 8px; vertical-align: 2px; }

  .back-pattern {
    position: absolute; inset: 0;
    background: radial-gradient(circle at 50% 45%, var(--orange) 0%, var(--orange-deep) 100%);
  }
  .back-mark {
    position: absolute; left: 0; right: 0; top: 440px; text-align: center;
    font-family: "Montserrat", sans-serif; font-weight: 800; color: var(--white);
    font-size: 14px; letter-spacing: 1px; text-transform: uppercase;
  }
</style>
</head>
<body>
<main class="canvas">
  <section class="card card--front">
    <div class="brand">
      <span class="brand__name">Steadfast<br>Vermin<br>Guard</span>
      <span class="brand__dot"></span>
    </div>

    <h1 class="holder">Gavin Holloway</h1>

    <div class="contact-rule">
      <span class="contact-rule__line"></span>
      <span class="icon" aria-label="Phone">
        <svg viewBox="0 0 24 24"><path fill="#1e1e20" d="M6.6 10.8a15 15 0 0 0 6.6 6.6l2.2-2.2c.3-.3.7-.4 1-.2 1.1.4 2.3.6 3.6.6.6 0 1 .4 1 1V20c0 .6-.4 1-1 1A17 17 0 0 1 3 4c0-.6.4-1 1-1h3.5c.6 0 1 .4 1 1 0 1.3.2 2.5.6 3.6.1.3 0 .7-.2 1l-2.3 2.2z"/></svg>
      </span>
      <span class="icon" aria-label="Email">
        <svg viewBox="0 0 24 24"><rect x="3" y="5" width="18" height="14" rx="1.5" fill="none" stroke="#1e1e20" stroke-width="2"/><path d="M3.5 6l8.5 7 8.5-7M3.5 18.5l6.5-6M20.5 18.5l-6.5-6" fill="none" stroke="#1e1e20" stroke-width="1.6"/></svg>
      </span>
      <span class="icon" aria-label="Website">
        <svg viewBox="0 0 24 24"><circle cx="12" cy="12" r="9" fill="none" stroke="#1e1e20" stroke-width="2"/><ellipse cx="12" cy="12" rx="4" ry="9" fill="none" stroke="#1e1e20" stroke-width="1.6"/><path d="M3 12h18" stroke="#1e1e20" stroke-width="1.6"/></svg>
      </span>
      <span class="contact-rule__line"></span>
    </div>

    <address class="contact" style="font-style:normal">
      <div class="contact__phone">0461 275 804</div>
      <div class="contact__email">Info@steadfastverminguard.com.au</div>
      <div class="contact__web">www.steadfastverminguard.com.au</div>
    </address>

    <div class="divider"></div>

    <section class="services">
      <h2 class="services__title">Services / Inspections</h2>
      <p class="services__list">
        Termites<span class="bullet"></span>Wood Borers<span class="bullet"></span>Ants<br>
        Cockroaches<span class="bullet"></span>Spiders<span class="bullet"></span>Fleas<span class="bullet"></span>Mice<br>
        Rats<span class="bullet"></span>Bed Bugs &amp; More!
      </p>
    </section>
  </section>

  <section class="card card--back">
    <div class="back-pattern" role="img" aria-label="Embossed repeating mascot pattern in tone-on-tone orange"></div>
    <div class="back-mark">Steadfast Vermin Guard</div>
  </section>
</main>
</body>
</html>
```